Harvest Gathering event flyer

I would like a church event flyer designed. The event is called "HARVEST GATHERING 2018". I am looking for a professional, yet catchy design that uses our brand colors and logo creatively while communicating key information of the event effectively.

1. The logo is attached in two color formats. The designer has the choice to use them as he/she want.

2. The location of the event is: Lindqvist Community Center, 482 Tamsworth Street, Portland, ME 04102
3. Time and date of event. The designer can organize and format the date and time as he/she pleases.
December 28th, 29th @ 7:00PM
December 30th @ 10:00AM
4. The topic of the event is "Tongues of fire". The designer is free to use this phrase as he/she pleases to create a good composition.
5. Speaker: Prophet Marcus Obuya
6. Contact information: contact@cedarbrookfellowship.org - Telephone number: 207 555 0148

7. I would also like the following three words on the flyer. These words describe the focus of the event: FIRE, REVIVAL, PROPHETIC

```html
<!DOCTYPE html>
<html lang="en">
<head>
<meta charset="utf-8">
<title>Harvest Gathering 2018</title>
<link href="https://fonts.googleapis.com/css2?family=Oswald:wght@600;700&family=Noto+Serif:wght@400;700&display=swap" rel="stylesheet">
<style>
  :root {
    --navy: #0f3660;
    --orange: #f7941d;
    --white: #ffffff;
    --stage: #6d6e71;
  }
  * { margin: 0; padding: 0; box-sizing: border-box; }
  html, body { width: 881px; height: 1200px; overflow: hidden; background: var(--stage); }
  .flyer {
    position: absolute; left: 53px; top: 51px; width: 774px; height: 1093px;
    background: var(--navy); overflow: hidden;
    box-shadow: 6px 6px 8px rgba(0,0,0,.35);
  }
  .flyer-frame {
    position: absolute; left: 11px; top: 16px; right: 12px; bottom: 10px;
    border: 2px dotted var(--orange); z-index: 5; pointer-events: none;
  }
  .line { position: absolute; left: 0; width: 100%; text-align: center; line-height: 1; transform: translateY(-50%); white-space: nowrap; }
  .condensed { font-family: "Oswald", sans-serif; font-weight: 700; }
  .serif { font-family: "Noto Serif", serif; font-weight: 700; }
  .event-title { top: 97px; color: var(--orange); font-size: 47px; letter-spacing: 3px; }
  .event-title span { display: inline-block; transform: scaleY(1.55); }
  .topic-banner { position: absolute; left: 63px; top: 169px; width: 644px; height: 124px; }
  .topic { top: 231px; color: var(--white); font-size: 60px; letter-spacing: -1px; }
  .rule { position: absolute; left: 162px; width: 460px; border-top: 2px dotted var(--orange); }
  .focus { top: 382px; color: var(--orange); font-size: 56px; }
  .focus span { display: inline-block; transform: scaleY(1.15); }
  .speaker-label { top: 474px; color: var(--white); font-size: 34px; }
  .speaker-name { top: 534px; color: var(--orange); font-size: 32px; font-weight: 700; letter-spacing: 1px; }
  .date-col { position: absolute; width: 340px; text-align: center; }
  .date-col.left { left: 27px; }
  .date-col.right { left: 404px; }
  .month { top: 619px; color: var(--white); font-size: 60px; letter-spacing: 9px; }
  .month span { display: inline-block; transform: scaleY(1.25); }
  .day { top: 697px; color: var(--orange); font-size: 42px; font-weight: 400; }
  .day span, .time span { display: inline-block; transform: scaleX(.82); }
  .time { top: 750px; color: var(--orange); font-size: 62px; font-weight: 400; }
  .date-divider { position: absolute; left: 387px; top: 585px; height: 164px; border-left: 3px dotted var(--orange); }
  .footer-wave { position: absolute; left: 0; top: 760px; width: 774px; height: 333px; }
  .brand { position: absolute; left: 40px; top: 930px; display: flex; align-items: center; gap: 10px; color: var(--navy); font-family: "Noto Serif", serif; font-weight: 700; font-size: 30px; }
  .brand-dot { width: 18px; height: 18px; border-radius: 50%; background: var(--orange); }
  .info-divider { position: absolute; left: 333px; top: 901px; height: 88px; border-left: 3px dotted var(--navy); }
  .venue { position: absolute; left: 373px; top: 896px; color: var(--navy); font-family: "Noto Serif", serif; font-weight: 700; font-size: 25px; line-height: 30.5px; font-style: normal; }
  .contact-band { position: absolute; left: 0; top: 1013px; width: 100%; height: 80px; background: var(--orange); }
  .contact { position: absolute; top: 20px; display: flex; align-items: center; gap: 10px; color: var(--navy); font-family: "Noto Serif", serif; font-weight: 700; font-size: 20px; white-space: nowrap; }
  .contact.phone { left: 45px; }
  .contact.email { left: 318px; }
  .contact svg { width: 36px; height: 36px; flex: none; }
</style>
</head>
<body>
<main class="flyer">
  <div class="flyer-frame"></div>

  <h1 class="line condensed event-title"><span>HARVEST GATHERING 2018</span></h1>

  <svg class="topic-banner" viewBox="0 0 644 124" aria-hidden="true">
    <path d="M62 6 H582 Q584 30 600 34 Q640 40 640 62 Q640 84 600 90 Q584 94 582 118 H62 Q60 94 44 90 Q4 84 4 62 Q4 40 44 34 Q60 30 62 6 Z" fill="var(--orange)" stroke="var(--white)" stroke-width="3"/>
  </svg>
  <h2 class="line serif topic">TONGUES OF FIRE</h2>

  <div class="rule" style="top:331px"></div>
  <p class="line condensed focus"><span>FIRE, REVIVAL, PROPHETIC</span></p>
  <div class="rule" style="top:432px"></div>

  <p class="line serif speaker-label">Speaker</p>
  <p class="line serif speaker-name">PROPHET MARCUS OBUYA</p>

  <div class="date-col left">
    <p class="line condensed month"><span>DECEMBER</span></p>
    <p class="line serif day"><span>28TH, 29TH @</span></p>
    <p class="line serif time"><span>7:00PM</span></p>
  </div>
  <div class="date-divider"></div>
  <div class="date-col right">
    <p class="line condensed month"><span>DECEMBER</span></p>
    <p class="line serif day"><span>30TH @</span></p>
    <p class="line serif time"><span>10:00AM</span></p>
  </div>

  <svg class="footer-wave" viewBox="0 0 774 333" aria-hidden="true">
    <path d="M0 13 C120 20 180 112 268 110 C370 108 430 22 523 25 C610 28 700 85 774 77 V333 H0 Z" fill="var(--white)" stroke="var(--orange)" stroke-width="5"/>
  </svg>

  <div class="brand"><span class="brand-dot"></span>CEDARBROOK</div>
  <div class="info-divider"></div>
  <address class="venue">
    Lindqvist Community Center<br>
    482 Tamsworth Street<br>
    Portland, ME 04102
  </address>

  <div class="contact-band">
    <div class="contact phone">
      <svg viewBox="0 0 36 36" aria-hidden="true">
        <circle cx="18" cy="18" r="16" fill="none" stroke="var(--navy)" stroke-width="2.5"/>
        <path d="M12 10 l4 4 -2 3 q2 4 6 6 l3 -2 4 4 -3 3 q-8 0 -14 -8 q-2 -4 -1 -7 z" fill="var(--navy)"/>
      </svg>
      207 555 0148
    </div>
    <div class="contact email">
      <svg viewBox="0 0 36 36" aria-hidden="true">
        <circle cx="18" cy="18" r="16" fill="none" stroke="var(--navy)" stroke-width="2.5"/>
        <rect x="9" y="12" width="18" height="12" fill="var(--navy)"/>
        <path d="M9 12 L18 19 L27 12 M9 24 L15.5 17.5 M27 24 L20.5 17.5" fill="none" stroke="var(--orange)" stroke-width="1.5"/>
      </svg>
      contact@cedarbrookfellowship.org
    </div>
  </div>
</main>
</body>
</html>
```